Lorraine Whitcombe Resume 2025

🎨 Design Aesthetic
Overall Look: Sophisticated, clean, minimalist — less “corporate template,” more “editorial/luxury brand.” Think Interiors Quarterly meets Pemberly Global Estates.
Colors:
Base: Warm white or ivory background (instead of stark white, which can feel clinical).
Accents: Soft taupe, blush beige, muted rose-gold, warm gray. These lean feminine, elegant, and upscale without being distracting.
Avoid heavy blacks — use charcoal gray for text.
🔤 Typography
You’ll want fonts that are timeless, system-available (no downloading), and upscale. Pairing one serif with one sans-serif is a proven high-end combo.
Primary Serif (for Name + Section Headers):
Georgia (classic, built-in)
Times New Roman (if you want ultra-traditional, though a bit expected)
Palatino Linotype (a softer, elegant serif)
Secondary Sans-serif (for body text):
Helvetica Neue (clean, luxury feel)
Calibri (simple, highly readable, professional)
Arial Narrow (refined but modern)
✨ Recommended pairing: Name/Headings in Georgia Bold + Body in Helvetica Neue Light → refined, professional, easy to use in all your collateral.
📐 Layout & Structure
Header (Top Third):
Your name large, centered or left-aligned.
Subline with phone, email, location in smaller font, spaced out with dividers (e.g., |).
Neutral line or subtle accent bar under the header (warm gray or muted blush).
Section Layout:
Plenty of white space (breathe between sections, upscale feel).
Clear section headers (all caps serif font, spaced letters for luxury look).
Use subtle horizontal rules in a soft accent color instead of thick lines.
Accents:
Very subtle shading in soft beige or blush for section backgrounds (not blocks, just highlights).
Icons kept minimal — avoid anything too “clip-arty.”
🖼 Visual Mood Reference
Imagine:
A high-end boutique hotel brand sheet
Valdine packaging tones (ivory, taupe, gold accent) but dialed down to be subtle
Editorial spacing like in Lustre or Nido Home
🗂 Sections to Highlight (for your pivot)
Profile / Objective – Short 2–3 lines at the top making clear you are pivoting into luxury real estate, with transferable leadership skills.
Experience – KTR Studio (as Owner, not Managing Partner) with emphasis on entrepreneurship, strategy, client growth.
Board Membership – Whitcombe Foundation role (philanthropy adds prestige).
Certifications – Shows discipline and learning.
Education – Clean, simple.
“I want a resume design that feels refined and luxury-oriented, clean and sophisticated, with soft neutral feminine tones (ivory, blush beige, taupe, warm gray). Font pairing should be elegant but standard (e.g., Georgia for headings + Helvetica Neue for body) so I can reuse across collateral without downloading special fonts. Layout should have lots of white space, understated lines/dividers, and feel like something you’d expect from a luxury real estate or fashion brand.”

```html
<!DOCTYPE html>
<html lang="en">
<head>
<meta charset="utf-8">
<title>Lorraine Whitcombe Resume</title>
<link rel="stylesheet" href="https://fonts.googleapis.com/css2?family=Open+Sans:wght@300;400;600;700&display=swap">
<style>
  :root{
    --backdrop:#d9d9d9;
    --paper:#ffffff;
    --blush:#fdf4ec;
    --accent-gray:#9a9c9b;
    --ink:#1b1b1b;
    --charcoal:#4a4a4a;
    --muted:#6e6e6e;
    --soft:#8a8a8a;
    --dot-off:#e2e2e2;
  }
  *{box-sizing:border-box;margin:0;padding:0}
  html,body{width:1200px;height:1200px;overflow:hidden}
  body{background:var(--backdrop);font-family:"Open Sans",Arial,sans-serif;color:var(--charcoal)}
  .page{position:absolute;left:189px;top:13px;width:822px;height:1174px;background:var(--paper);overflow:hidden}
  .page > *{position:absolute}
  .corner-block{left:0;top:0;width:66px;height:65px;background:var(--accent-gray)}
  .sidebar{left:0;top:65px;width:287px;height:1067px;background:var(--blush)}
  .portrait{left:66px;top:65px;width:184px;height:220px;background:radial-gradient(ellipse at 50% 40%,#bdbdbd 0%,#9a9a9a 45%,#3e3e3e 100%)}
  .name{left:66px;top:302px;width:215px;font-size:18.2px;font-weight:700;color:#6b6b6b;letter-spacing:0;white-space:nowrap}
  .title{left:66px;top:326px;font-size:11px;color:var(--soft)}
  .side-head{font-size:14.5px;font-weight:400;color:var(--ink);letter-spacing:.3px}
  .side-head.light{color:var(--muted)}
  .small{font-size:11.6px;line-height:16px;color:var(--charcoal)}
  .contact-row{left:62px;width:220px;height:16px;font-size:11.6px;color:var(--muted)}
  .contact-row svg{position:absolute;left:0;top:2px;width:12px;height:12px}
  .contact-row span{position:absolute;left:42px;top:0;white-space:nowrap}
  .side-icon{width:17px;height:15px}
  .school{font-size:12px;font-weight:700;color:#5c5c5c;letter-spacing:.3px}
  .skill{left:64px;width:200px;height:14px}
  .skill .label{position:absolute;left:0;top:0;color:var(--muted);white-space:nowrap}
  .skill .dots{position:absolute;left:138px;top:4px;display:flex;gap:6px}
  .skill .dots i{width:7px;height:7px;border-radius:50%;background:#4f4f4f}
  .skill .dots i.off{background:var(--dot-off)}
  .main-head{font-size:16px;font-weight:300;color:var(--ink);letter-spacing:.2px}
  .main-head.sm{font-size:14.5px;font-weight:400}
  .body-text{font-size:11.6px;line-height:15.7px;color:var(--muted);text-align:justify}
  .body-text.dark{color:var(--charcoal)}
  .timeline{width:1.5px;background:var(--ink)}
  .node{width:7px;height:7px;border-radius:50%;background:var(--ink)}
  .org{font-size:17.6px;font-weight:700;color:var(--ink);white-space:nowrap}
  .org.board{font-size:16.6px}
  .dates{font-size:14.4px;color:var(--charcoal);white-space:nowrap}
  .role{font-size:13.6px;color:var(--ink)}
  .key{font-size:12.8px;font-weight:700;color:var(--muted)}
  .bullet{left:376px;width:380px;font-size:11.6px;line-height:20px;color:var(--muted);text-align:justify}
  .bullet::before{content:"•";margin-right:8px;font-size:10px}
  .board-role{left:372px;top:990px;width:420px;font-size:14px;line-height:22px;color:var(--soft);text-transform:uppercase}
  .footer-bar{left:61px;top:1132px;width:737px;height:12px;background:#9a9a9a}
</style>
</head>
<body>
<main class="page">
  <div class="corner-block"></div>
  <aside class="sidebar"></aside>
  <div class="portrait" role="img" aria-label="Portrait photograph of Lorraine Whitcombe"></div>

  <h1 class="name">LORRAINE WHITCOMBE</h1>
  <p class="title">TITLE</p>

  <h2 class="side-head" style="left:62px;top:380px">CONTACTS</h2>
  <p class="small" style="left:62px;top:408px">218 Linden Crest Lane<br>Fairbrook, TN&nbsp; 37000</p>

  <div class="contact-row" style="top:451px">
    <svg viewBox="0 0 12 12"><rect x="0.5" y="2" width="11" height="8" fill="#1b1b1b"/><path d="M0.5 2 L6 6.5 L11.5 2" stroke="#fdf4ec" fill="none"/></svg>
    <span>Lorraine@ktrstudio.com</span></div>
  <div class="contact-row" style="top:474px">
    <svg viewBox="0 0 12 12"><path d="M2.5 0.8 L4.6 3.4 L3.4 4.8 C4.2 6.6 5.4 7.8 7.2 8.6 L8.6 7.4 L11.2 9.5 L9.8 11.2 C5 10.6 1.4 7 0.8 2.2 Z" fill="#1b1b1b"/></svg>
    <span style="color:#3a3a3a">(555) 410-3827</span></div>
  <div class="contact-row" style="top:494px">
    <svg viewBox="0 0 12 12" fill="none" stroke="#1b1b1b" stroke-width="1"><circle cx="6" cy="6" r="5.2"/><ellipse cx="6" cy="6" rx="2.3" ry="5.2"/><path d="M0.8 6 H11.2 M1.8 3.3 H10.2 M1.8 8.7 H10.2"/></svg>
    <span>www.lorrainewhitcombe.com</span></div>
  <div class="contact-row" style="top:513px">
    <svg viewBox="0 0 12 12"><rect x="0.5" y="0.5" width="11" height="11" fill="#1b1b1b"/></svg>
    <span>profile/ lorrainewhitcombe</span></div>

  <svg class="side-icon" style="left:62px;top:578px" viewBox="0 0 17 15" fill="none" stroke="#1b1b1b" stroke-width="1.3"><path d="M8.5 3 C6 1.5 3.5 1.5 1 2.2 V12.5 C3.5 11.8 6 11.8 8.5 13.2 C11 11.8 13.5 11.8 16 12.5 V2.2 C13.5 1.5 11 1.5 8.5 3 Z M8.5 3 V13.2"/></svg>
  <h2 class="side-head light" style="left:99px;top:576px">EDUCATION</h2>
  <p class="school" style="left:62px;top:614px">HALVERTON UNIVERSITY</p>
  <p class="small" style="left:63px;top:637px;line-height:18px">Bachelor of Arts, Sociology<br>1993 – 1998</p>
  <p class="small" style="left:62px;top:710px;width:200px;line-height:18.2px;color:#2f2f2f">Ashford Valley University, Ashford, Ohio, Bachelor of Business Administration with an emphasis on Healthcare Administration.</p>

  <svg class="side-icon" style="left:63px;top:836px" viewBox="0 0 17 15" fill="none" stroke="#1b1b1b" stroke-width="1.2"><path d="M1 0.5 V14 H16.5"/><path d="M3 11 L6 6 L8.5 8.5 L11 4 L13 6.5 L15.5 2.5"/></svg>
  <h2 class="side-head" style="left:101px;top:834px">SKILLS</h2>

  <div class="skill" style="top:883px"><span class="label" style="font-size:11.6px">Collaboration</span><span class="dots"><i></i><i></i><i></i><i class="off"></i><i class="off"></i></span></div>
  <div class="skill" style="top:914px"><span class="label" style="font-size:11.6px">Leadership</span><span class="dots"><i></i><i></i><i></i><i class="off"></i><i class="off"></i></span></div>
  <div class="skill" style="top:946px"><span class="label" style="font-size:10px">Communication</span><span class="dots"><i></i><i></i><i></i><i class="off"></i><i class="off"></i></span></div>
  <div class="skill" style="top:974px"><span class="label" style="font-size:10px">Organizational</span><span class="dots"><i></i><i></i><i></i><i class="off"></i><i class="off"></i></span></div>
  <div class="skill" style="top:1001px"><span class="label" style="font-size:10px">People Skills</span><span class="dots"><i></i><i></i><i></i><i class="off"></i><i class="off"></i></span></div>
  <div class="skill" style="top:1028px"><span class="label" style="font-size:10px">Problem solving abilities</span><span class="dots"><i></i><i></i><i></i><i class="off"></i><i class="off"></i></span></div>

  <svg style="left:336px;top:170px;width:18px;height:18px" viewBox="0 0 18 18" fill="#1b1b1b"><circle cx="9" cy="5" r="4"/><path d="M1 17 C1 11.5 4.5 9.5 9 9.5 C13.5 9.5 17 11.5 17 17 Z"/></svg>
  <h2 class="main-head" style="left:373px;top:168px">PERSONAL PROFIL</h2>
  <p class="body-text" style="left:336px;top:215px;width:397px">Lorraine Whitcombe is an industry-leading media strategist and entrepreneur with 15+ years of experience across multiple industries. As Owner of the award-winning EDWOSB-certified agency KTR Studio Inc., she drives performance across multiple departments and acts as an internal strategic advisor. Her expertise spans government project management and corporate workflows, providing a rare combination of entrepreneurship, leadership, and marketing strategy.</p>
  <p class="body-text" style="left:336px;top:341px;width:397px">Lorraine is now pursuing a full-time career in real estate, bringing her skills in negotiation, business development, and client relations to the Miami luxury market.</p>

  <svg style="left:335px;top:450px;width:17px;height:17px" viewBox="0 0 17 17" fill="#1b1b1b"><path d="M6 1 H11 V3 H10 V2 H7 V3 H6 Z"/><rect x="1" y="3.5" width="15" height="12" rx="1.5"/><rect x="1" y="8" width="15" height="1.2" fill="#fff"/></svg>
  <h2 class="main-head sm" style="left:376px;top:450px">WORK EXPERIENCE</h2>
  <div class="timeline" style="left:344px;top:476px;height:429px"></div>
  <div class="node" style="left:341px;top:491px"></div>
  <p class="org" style="left:378px;top:481px">KTR STUDIO, INC.</p>
  <p class="dates" style="left:653px;top:488px">2007 – Present</p>
  <p class="role" style="left:379px;top:506px">OWNER</p>
  <p class="body-text dark" style="left:376px;top:537px;width:380px">As a business owner in the media and marketing space, Lorraine brings innovative insight and marketing ideas, becoming an industry expert for every client. Her creativity, flexibility, transparency, and results-driven approach lend to long-term partnerships across all business verticals. By working closely with clients, her teams create powerful media and marketing campaigns that engage and inspire.</p>
  <p class="key" style="left:376px;top:646px">Key Accomplishments</p>
  <p class="bullet" style="top:677px">Scaled KTR Studio Inc.’s client base both commercially and federally during the COVID-19 pandemic.</p>
  <p class="bullet" style="top:728px">Conceptualized and organized large-scale campaigns while leading KTR to immense success despite market disruptions.</p>
  <p class="bullet" style="top:779px">Directed Harborline Civic Service campaigns across 13+ states in the past 12 months.</p>
  <p class="bullet" style="top:830px;line-height:15.7px;padding-top:2px">For the Lakeshore Civic Service, overhauled marketing efforts to be data-driven and high-performing, delivering 3M+ impressions, 700+ conversions (2.58% conversion rate), and a 533% decreased CPA (from $901 to $48 at launch).</p>

  <svg style="left:329px;top:931px;width:20px;height:14px" viewBox="0 0 20 14" fill="#1b1b1b"><circle cx="10" cy="3.5" r="3"/><circle cx="4" cy="5" r="2.3"/><circle cx="16" cy="5" r="2.3"/><path d="M4.5 14 C4.5 9.5 7 7.5 10 7.5 C13 7.5 15.5 9.5 15.5 14 Z"/><path d="M0 13 C0 9.5 1.8 8 4 8 C5 8 5.5 8.3 6 8.6 C4.8 10 4.2 11.5 4 13 Z M20 13 C20 9.5 18.2 8 16 8 C15 8 14.5 8.3 14 8.6 C15.2 10 15.8 11.5 16 13 Z"/></svg>
  <h2 class="main-head sm" style="left:373px;top:936px">BOARD MEMBERSHIP</h2>
  <div class="timeline" style="left:344px;top:955px;height:129px"></div>
  <div class="node" style="left:341px;top:974px"></div>
  <p class="org board" style="left:372px;top:963px">THE WHITCOMBE FOUNDATION</p>
  <p class="dates" style="left:668px;top:967px">2018 – Present</p>
  <p class="board-role">Active board member, the Sylvia Whitcombe &amp; William W. Whitcombe Memorial Foundation</p>
  <p class="body-text dark" style="left:372px;top:1055px;width:410px;line-height:18.5px;text-align:left">Support governance, fundraising, and philanthropic initiatives dedicated to advancing music education and instrument preservation.</p>

  <div class="footer-bar"></div>
</main>
</body>
</html>
```